【 概要 】 私が運営しているサイトのブログのアイキャッチ制作です。 https://voyamiro.asia/ 【 依頼内容 】 ・サイズ: 横728px × 縦485 ・作成数: 1種類 ・利用用途:Webサイト 【 デザインイメージ 】 ・写真に合ったデザインでお願いします。 【素材】 写真は2点を用意しています。 どちらか1点を使っていただいてもいいですし、2点を組み合わせてもらってもけっこうです。 【入れていただきたいテキスト】 ◆大キャッチ◆ タイ旅行で知っておかないと危ない 10のコト |
写真2枚を上手く使い、視認性の高いデザインに仕上げていただいたので採用しました。
この度はデザインをご提案いただきありがとうございました。
今後も同様のお仕事を発注してまいりますので、また機会がありましたらよろしくお願いいたします。

```html
<!DOCTYPE html>
<html lang="ja">
<head>
<meta charset="UTF-8">
<title>タイ旅行で知っておかないと危ない10のコト</title>
<link rel="stylesheet" href="https://fonts.googleapis.com/css2?family=Yusei+Magic&display=swap">
<style>
  :root {
    --sky: #7fb6e6;
    --sky-light: #dbeaf4;
    --street: #7d8387;
    --paper: #ecebcf;
    --paper-line: rgba(110, 135, 110, 0.28);
    --paper-shadow: rgba(0, 0, 0, 0.3);
    --ink: #5b2467;
    --ink-outline: #ffffff;
    --accent: #e5338f;
    --warn: #f7d21c;
    --flag-red: #e0252f;
    --flag-white: #ffffff;
    --flag-blue: #23307a;
    --hole: #6f7f86;
  }
  * { margin: 0; padding: 0; box-sizing: border-box; }
  html, body { width: 1200px; height: 800px; overflow: hidden; }
  body { position: relative; background: var(--sky-light); font-family: "Yusei Magic", sans-serif; }

  .street-scene {
    position: absolute; inset: 0;
    background:
      linear-gradient(90deg, rgba(40, 110, 60, 0.35) 0%, transparent 12%, transparent 78%, rgba(226, 196, 110, 0.8) 92%),
      linear-gradient(180deg, var(--sky) 0%, var(--sky-light) 38%, #a9b0b4 58%, var(--street) 100%);
  }

  .notebook {
    position: absolute; left: 82px; top: 58px; width: 640px; height: 640px;
    transform: rotate(-2deg);
    background:
      repeating-linear-gradient(0deg, var(--paper-line) 0 1px, transparent 1px 30px),
      repeating-linear-gradient(90deg, var(--paper-line) 0 1px, transparent 1px 30px),
      var(--paper);
    box-shadow: 6px 8px 18px var(--paper-shadow);
  }
  .notebook__holes {
    position: absolute; left: 10px; top: 18px; bottom: 18px; width: 22px;
    background: radial-gradient(circle at 11px 11px, var(--hole) 7px, transparent 8px) 0 0 / 22px 38px repeat-y;
  }
  .notebook__photo {
    position: absolute; left: 40px; top: 140px; width: 580px; height: 360px;
    background: linear-gradient(180deg, rgba(150, 180, 110, 0.45), rgba(200, 170, 100, 0.4) 55%, rgba(110, 130, 100, 0.4));
  }

  .tuk-tuk {
    position: absolute; left: 700px; top: 180px; width: 460px; height: 600px;
    background: linear-gradient(180deg, #e2b23a 0%, #3559a8 35%, #2d4288 72%, #3a3a3e 100%);
  }

  .headline { position: absolute; inset: 0; color: var(--ink); font-weight: 400; }
  .headline span {
    position: absolute; white-space: nowrap; line-height: 1;
    -webkit-text-stroke: 10px var(--ink-outline); paint-order: stroke fill;
    transform: rotate(-3deg); transform-origin: left center;
  }
  .headline__line1 { left: 210px; top: 122px; font-size: 80px; }
  .headline__line2 { left: 178px; top: 262px; font-size: 62px; }
  .headline__line3 { left: 400px; top: 352px; font-size: 92px; }
  .headline__line4 { left: 230px; top: 500px; font-size: 80px; }
  .headline__num { font-weight: 400; font-size: 150px; color: var(--accent); vertical-align: -22px; margin-right: 4px; }

  .warning-icon { position: absolute; left: 322px; top: 392px; width: 76px; height: 70px; }
  .flag { position: absolute; left: 574px; top: 86px; width: 184px; height: 122px; transform: rotate(-8deg); }
  .accent-dashes { position: absolute; left: 636px; top: 470px; width: 70px; height: 72px; }
  .pen {
    position: absolute; left: 196px; top: 540px; width: 56px; height: 230px;
    transform: rotate(-24deg);
    background: #2e63b4;
  }
</style>
</head>
<body>
  <div class="street-scene" role="img" aria-label="バンコクの街角と黄色い建物、青空の写真"></div>

  <div class="notebook">
    <div class="notebook__holes"></div>
    <div class="notebook__photo" role="img" aria-label="タイの寺院と街並みの淡い写真"></div>
  </div>

  <div class="tuk-tuk" role="img" aria-label="街角に停まる青と黄色のトゥクトゥクの写真"></div>

  <h1 class="headline">
    <span class="headline__line1">タイ旅行で</span>
    <span class="headline__line2">知っておかないと</span>
    <span class="headline__line3">危ない</span>
    <span class="headline__line4"><b class="headline__num">10</b>のコト</span>
  </h1>

  <svg class="warning-icon" viewBox="0 0 84 76" aria-hidden="true">
    <path d="M42 4 L80 72 L4 72 Z" fill="var(--warn)" stroke="var(--ink-outline)" stroke-width="5" stroke-linejoin="round"/>
    <rect x="38" y="26" width="8" height="26" rx="3" fill="#222"/>
    <circle cx="42" cy="61" r="4.5" fill="#222"/>
  </svg>

  <svg class="flag" viewBox="0 0 180 120" aria-label="タイの国旗">
    <rect x="0" y="0" width="180" height="20" fill="var(--flag-red)"/>
    <rect x="0" y="20" width="180" height="20" fill="var(--flag-white)"/>
    <rect x="0" y="40" width="180" height="40" fill="var(--flag-blue)"/>
    <rect x="0" y="80" width="180" height="20" fill="var(--flag-white)"/>
    <rect x="0" y="100" width="180" height="20" fill="var(--flag-red)"/>
  </svg>

  <svg class="accent-dashes" viewBox="0 0 70 72" aria-hidden="true">
    <path d="M8 40 L44 8" stroke="var(--warn)" stroke-width="6" stroke-linecap="round"/>
    <path d="M22 62 L64 40" stroke="var(--warn)" stroke-width="6" stroke-linecap="round"/>
  </svg>

  <div class="pen" role="img" aria-label="青い万年筆のイラスト"></div>
</body>
</html>
```